Internationally renowned speaker/campaigner needs a book cover

I need a preliminary cover design for my new book "HALF-LIGHT".

I'm a medical doctor and an internationally renowned speaker and campaigner for human-centered and compassionate healthcare, co-founder of an international social movement KINDLING in CLINICS (http://kindlinginclinics.example), and successful author of the book 'PAUSE AND LISTEN - Ways to cherish your practice and your people' (http://www.bookvaultstore.example/PAUSE-LISTEN-cherish-your-practice/dp/9082614530)

The subtitle of HALF-LIGHT is: "How our half-sighted mechanical science breeds division, hoarding, scarcity, conflict, ill-being and the unravelling of nature (and what we can do instead)"

Author: Dr GARETH PELLIMORE

Preliminary book blurb:
"As social activists and environmental campaigners we are continuously sabotaging our cause because our strategies are unconsciously supporting the materialistic foundations of our broken world.

Our materialistic science sees the natural world and even people as innate objects, without consciousness or connection. Modern medicine treats patients as broken machines to be fixed, not as conscious, subjective beings. And economic theory says every person is an independent agent, striving to maximize advantage. We turn every human and natural gift into a commodity to be owned, controlled, bought and sold.

Our social policies, education system, justice system and even our democracy assume that incentives, rewards and punishments are the ‘real’ motives for human behavior. Our purpose in life is to ‘get ahead’ and accumulate material goods. Therein lies competition, insecurity, greed, violence, ill-health and the destruction of the natural environment.

Materialistic science is simply blind to the life-world of consciousness, intelligence, purpose and deep interdependence in all natural and human systems. We all know that compassion, kindness, love, and human creativity are the real foundation of our communities, not mindless competition.

But so immersed are we in materialistic assumptions, that in our campaigns we mistakenly adopt tools and strategies from the existing system in our struggle for a better world. But the moment we fight against anything, or demonize our opposition, or sell our ideas for money, or charitably impose our solutions, we only strengthen the material world.

Instead, we have to be the change we want to see: grow an economy of generosity and gifting, freely share ideas, focus on solutions not problems, and deeply believe in the capacity for creativity and healing in every person and every community. You can download this book for free at halflightbook.org."

Design brief
I need a compelling front page image and title design that conveys the idea that our science is one-eyed or half-blind, hence the title name 'half-light', which means half-science.

Our predominant science only sees the material world, not the conscious world. We need both.

I'm also preparing a IDEAx talk on the subject and want the compelling image and title to use for this purpose also.

The genre of books is in the class of leadership, entrepreneurs, positive psychology, community development - and I have uploaded some cover images of books in this class. The cover of my current book, PAUSE AND LISTEN, has elements of the style I'm looking for: bold, bright, simple, metaphorical, a surprising juxtaposition of technical and human.

The way I develop and market the book will be congruent with the ideas expressed. I will give the e-book away for free and invite people to make a donation if they like it (gift economy). The book will be published on the website unfinished, inviting comments, suggestions, stories and ideas to be included in the finished book. So to a degree, the content of the book will be fully developed by crowdsourcing living examples of the core ideas and creating a community of conversation (including a Chatterly page). I'll later be looking for a simple WordPress website design based on the book cover graphic, fonts and colours.

So this first design brief and contract is for an e-book cover and later the book will be self-published as a paperback using PressNest.

Target Market(s)

The target audience is readers who are community leaders and social activists - all those utterly passionate about creating a better world, whether it's in the environment, education, healthcare, violence prevention, justice, health communities, etc.

Font styles to use
Sans Serif

Requirements
Must have
• A compelling image that symbolises the key idea - eyecatching
Should not have
• Must not express 'corporate' concepts, power or hierarchy

```html
<!DOCTYPE html>
<html lang="en">
<head>
<meta charset="utf-8">
<title>HALF-LIGHT — Dr Gareth Pellimore</title>
<link rel="stylesheet" href="https://fonts.googleapis.com/css2?family=Barlow+Condensed:wght@300;600&family=Montserrat:wght@900&family=Big+Shoulders+Stencil+Display:wght@600&display=swap">
<style>
  :root {
    --paper: #f4f4ef;
    --grid: #d9d8ec;
    --blue: #1b6bbb;
    --orange: #ffa000;
    --white: #ffffff;
    --brain-grey: #dcdcdc;
  }
  html, body {
    margin: 0;
    padding: 0;
    overflow: hidden;
    background: var(--paper);
  }
  .cover {
    position: relative;
    width: 808px;
    height: 1200px;
    overflow: hidden;
    background-color: var(--paper);
    background-image:
      linear-gradient(to right, var(--grid) 1px, transparent 1px),
      linear-gradient(to bottom, var(--grid) 1px, transparent 1px);
    background-size: 22px 22px;
  }
  .cover-art {
    position: absolute;
    inset: 0;
    width: 808px;
    height: 1200px;
  }
  .band-blue { fill: var(--blue); }
  .band-orange { fill: var(--orange); }
  .subtitle {
    font-family: "Barlow Condensed", sans-serif;
    fill: var(--white);
    font-size: 36px;
  }
  .subtitle-light { font-weight: 300; }
  .subtitle-bold { font-weight: 600; }
  .title {
    font-family: "Montserrat", sans-serif;
    font-weight: 900;
    font-size: 100px;
    stroke: var(--white);
    stroke-width: 12px;
    stroke-linejoin: round;
    paint-order: stroke fill;
  }
  .title-first { fill: var(--orange); }
  .title-second { fill: var(--blue); }
  .author {
    font-family: "Big Shoulders Stencil Display", sans-serif;
    font-weight: 600;
    font-size: 46px;
  }
  .author-first { fill: var(--white); }
  .author-last { fill: var(--blue); }
</style>
</head>
<body>
<main class="cover">
  <svg class="cover-art" viewBox="0 0 808 1200" xmlns="http://www.w3.org/2000/svg">
    <defs>
      <linearGradient id="brain-tones" x1="0" y1="0" x2="1" y2="0">
        <stop offset="0" stop-color="#1b6bbb"/>
        <stop offset="0.49" stop-color="#1b6bbb"/>
        <stop offset="0.5" stop-color="#f4f4ef"/>
        <stop offset="0.52" stop-color="#f4f4ef"/>
        <stop offset="0.53" stop-color="#dcdcdc"/>
        <stop offset="1" stop-color="#dcdcdc"/>
      </linearGradient>
    </defs>

    <!-- top header bands -->
    <polygon class="band-orange" points="0,80 808,44 808,80"/>
    <rect class="band-blue" x="0" y="80" width="808" height="228"/>
    <polygon class="band-orange" points="0,308 808,308 808,316 0,340"/>

    <!-- subtitle -->
    <g class="subtitle">
      <text class="subtitle-light" x="90" y="138" textLength="628" lengthAdjust="spacingAndGlyphs">HOW OUR HALF-SIGHTED MECHANICAL SCIENCE BREEDS</text>
      <text class="subtitle-bold" x="68" y="184" textLength="672" lengthAdjust="spacingAndGlyphs">DIVISION, HOARDING, SCARCITY, CONFLICT, ILL-BEING</text>
      <text class="subtitle-bold" x="174" y="230" textLength="460" lengthAdjust="spacingAndGlyphs">AND THE UNRAVELLING OF NATURE</text>
      <text class="subtitle-light" x="214" y="274" textLength="381" lengthAdjust="spacingAndGlyphs">(AND WHAT WE CAN DO INSTEAD)</text>
    </g>

    <!-- title -->
    <text class="title" x="64" y="468" textLength="684" lengthAdjust="spacingAndGlyphs"><tspan class="title-first">HALF-</tspan><tspan class="title-second">LIGHT</tspan></text>

    <!-- central brain illustration area -->
    <rect x="146" y="518" width="516" height="456" rx="200" ry="210" fill="url(#brain-tones)" role="img" aria-label="Illustration of a brain split in two: the left half blue with white science icons, the right half plain light grey"/>

    <!-- bottom author bands -->
    <polygon class="band-blue" points="0,1012 808,1038 0,1038"/>
    <rect class="band-orange" x="0" y="1038" width="808" height="86"/>
    <polygon class="band-blue" points="0,1124 808,1124 808,1148"/>

    <!-- author -->
    <text class="author" x="200" y="1098" textLength="408" lengthAdjust="spacingAndGlyphs"><tspan class="author-first">Dr. GARETH </tspan><tspan class="author-last">PELLIMORE</tspan></text>
  </svg>
</main>
</body>
</html>
```